Business Card Design

i need a business card to promote my Handyman & Gardening business. It would be nice to see a design incorporating both of these things. We are happy to help in any way we can with no job ever being to small.

Industry/Entity Type

Business

Contact Information for Business Card

Dave's Handyman & Gardening Service
Dave Holt
PO Box 312 Wrenford SA 5461
dave.holt@fernmail.com
ph 0412 736 508

```html
<!DOCTYPE html>
<html lang="en">
<head>
<meta charset="utf-8">
<title>Dave's Handyman &amp; Gardening Service – Business Card</title>
<link rel="stylesheet" href="https://fonts.googleapis.com/css2?family=Quicksand:wght@300;400&display=swap">
<style>
  :root {
    --ink: #000000;
    --paper: #ffffff;
    --text: #111111;
  }
  * { margin: 0; padding: 0; box-sizing: border-box; }
  html, body {
    width: 1200px;
    height: 739px;
    overflow: hidden;
    background: var(--paper);
  }
  .card {
    position: relative;
    width: 1200px;
    height: 739px;
    background: var(--paper);
    font-family: "Quicksand", sans-serif;
    color: var(--text);
  }
  .brand-band {
    position: absolute;
    left: 0;
    top: 0;
    width: 1200px;
    height: 309px;
    background: var(--ink);
  }
  .brand-name {
    position: absolute;
    top: 92px;
    left: 0;
    width: 1200px;
    height: 152px;
    color: var(--paper);
    font-weight: 300;
    font-size: 62px;
    line-height: 76px;
    letter-spacing: 0.5px;
    text-transform: uppercase;
  }
  .brand-name .col-left {
    position: absolute;
    right: 578px;
    top: 0;
    text-align: right;
  }
  .brand-name .joiner {
    position: absolute;
    left: 682px;
    top: 38px;
  }
  .brand-name .col-right {
    position: absolute;
    left: 780px;
    top: 0;
    text-align: left;
  }
  .brand-name span { display: block; white-space: nowrap; }

  .contact {
    position: absolute;
    left: 40px;
    top: 538px;
  }
  .contact-name {
    font-weight: 400;
    font-size: 50px;
    line-height: 60px;
    letter-spacing: 1px;
    margin-bottom: 4px;
  }
  .contact-details {
    font-style: normal;
    font-weight: 400;
    font-size: 31px;
    line-height: 34px;
  }
  .contact-details span { display: block; white-space: nowrap; }
</style>
</head>
<body>
  <div class="card">
    <header class="brand-band">
      <h1 class="brand-name" aria-label="Dave's Handyman &amp; Gardening Service">
        <span class="col-left"><span>Dave's</span><span>Handyman</span></span>
        <span class="joiner">&amp;</span>
        <span class="col-right"><span>Gardening</span><span>Service</span></span>
      </h1>
    </header>

    <section class="contact">
      <p class="contact-name">Dave Holt</p>
      <address class="contact-details">
        <span>PO Box 312 Wrenford SA 5461</span>
        <span>0412 736 508</span>
        <span>dave.holt@fernmail.com</span>
      </address>
    </section>
  </div>
</body>
</html>
```